CD Artwork for the band Bayou Lanternmen

A fun, smokin' hot zydeco band needs album art for second CD, using the attached templates.
Band Name: Bayou Lanternmen
Album Title: "Bayou Lanternmen II" (or "Bayou Lanternmen 2", or "Bayou Lanternmen Q" with the script Q resembling the number 2)
You can follow your muse and use any of the attached photos.
Here are the panels we need designed:
1) Front CD cover - could be single photo or a collage of photos
2) Back CD cover - could be single photo or a collage of photos
3) Inside Panel - could be single photo or a collage of photos
4) Inside Panel that CD rests on - could be single photo or a collage of photos
5) CD disc face
***Must incorporate our logo on either the front or back cover,
and on the disc face ***
A bit about the band:
Bayou Lanternmen play hot Louisiana-flavored dance music. Sweet Cajun accordion, electric guitar and a powerhouse rhythm section, and that cool metal rubboard vest! Bring yer dancin’ shoes...
And these guidelines from our printer:
When sending your PDF images: Did you use the supplied templates from the project center? Old templates will cause the image to appear to “shift” in the proof. Do NOT crop the template in any way before uploading your image. (The extra “white space” surrounding the template is necessary in centering your images properly)
Be sure to “hide” or “remove” your template guides before exporting.
Be sure to “save” your image as a PDF. We strongly recommend that you export your PDF using the “PDF/X-4” settings in the PDF Export dialog box. Do not “print” as a pdf. This will show your image has shifted in the template, because it is sizing the image to the print size of 8½ x 11.
Be sure that your artwork extends into the crop marks. All text must remain inside the safety areas. Disc images should be uploaded as a “square” for optimal coverage. Do not leave a center hole cut out.
Images should be set at 300dpi or greater or will appear "grainy" or "pixelated".
Thanks - can't wait to see what you come up with!
Target Market(s)
music lovers, cowboys & cowgirls, fun lovers, party
Colors
Designer to choose colors to be used in the design.
Look and feel
Each slider illustrates characteristics of the customer's brand and the style your logo design should communicate.

```html
<!DOCTYPE html>
<html lang="en">
<head>
<meta charset="utf-8">
<title>Bayou Lanternmen – Front Cover</title>
<link rel="stylesheet" href="https://fonts.googleapis.com/css2?family=Archivo+Black&family=Oswald:wght@700&display=swap">
<style>
  :root {
    --paper: #ffffff;
    --navy: #161a86;
    --gold: #f5b700;
    --photo-sky: #5fa9cc;
    --photo-teal: #3c8fb5;
    --photo-red: #b0442a;
    --photo-brass: #c9a03c;
    --photo-haze: #d8e8ee;
  }
  html, body {
    margin: 0;
    padding: 0;
    width: 1200px;
    height: 1200px;
    overflow: hidden;
    background: var(--paper);
  }
  .cover {
    position: relative;
    width: 1200px;
    height: 1200px;
    background: var(--paper);
    overflow: hidden;
  }
  .cover-art {
    position: absolute;
    inset: 0;
    width: 1200px;
    height: 1200px;
  }
  .band-mark {
    position: absolute;
    top: 40px;
    right: 44px;
    display: flex;
    align-items: center;
    gap: 14px;
    font-family: "Oswald", sans-serif;
    font-weight: 700;
    font-size: 40px;
    line-height: 1;
    color: var(--navy);
    text-transform: uppercase;
  }
  .band-mark-dot {
    width: 34px;
    height: 34px;
    border-radius: 50%;
    background: var(--navy);
  }
  .album-title {
    position: absolute;
    left: 68px;
    top: 1060px;
    margin: 0;
    font-family: "Oswald", sans-serif;
    font-weight: 700;
    font-style: italic;
    font-size: 82px;
    line-height: 1;
    letter-spacing: 1px;
    color: var(--gold);
    white-space: nowrap;
  }
</style>
</head>
<body>
  <main class="cover">
    <svg class="cover-art" viewBox="0 0 1200 1200" xmlns="http://www.w3.org/2000/svg">
      <defs>
        <linearGradient id="photo-tones" x1="0" y1="0" x2="1" y2="0.6">
          <stop offset="0" stop-color="var(--photo-red)"/>
          <stop offset="0.3" stop-color="var(--photo-brass)"/>
          <stop offset="0.55" stop-color="var(--photo-brass)"/>
          <stop offset="0.75" stop-color="var(--photo-teal)"/>
          <stop offset="1" stop-color="var(--photo-haze)"/>
        </linearGradient>
        <linearGradient id="photo-sky" x1="0" y1="0" x2="0" y2="1">
          <stop offset="0" stop-color="var(--photo-sky)" stop-opacity="0.85"/>
          <stop offset="0.35" stop-color="var(--photo-sky)" stop-opacity="0"/>
        </linearGradient>
      </defs>
      <g class="cover-photo" role="img" aria-label="Photograph: close-up of a player's hands on a red and brass Cajun button accordion, blue patterned shirt behind">
        <path d="M0 0 H1200 V620 L1160 640 L1130 625 L1100 660 L1060 640 L1030 700 L990 670 L950 720 L900 700 L860 760 L820 730 L770 790 L720 760 L680 820 L640 800 L590 850 L540 830 L500 880 L450 860 L400 900 L350 880 L300 910 L250 890 L200 920 L150 900 L100 930 L50 905 L0 930 Z" fill="url(#photo-tones)"/>
        <path d="M0 0 H1200 V620 L1160 640 L1130 625 L1100 660 L1060 640 L1030 700 L990 670 L950 720 L900 700 L860 760 L820 730 L770 790 L720 760 L680 820 L640 800 L590 850 L540 830 L500 880 L450 860 L400 900 L350 880 L300 910 L250 890 L200 920 L150 900 L100 930 L50 905 L0 930 Z" fill="url(#photo-sky)"/>
      </g>
      <text class="album-q" x="1205" y="1130" text-anchor="end" font-family="'Archivo Black', sans-serif" font-size="830" fill="var(--navy)">Q</text>
    </svg>

    <div class="band-mark">
      <span class="band-mark-dot"></span>
      <span>Bayou Lanternmen</span>
    </div>

    <h1 class="album-title">Bayou Lanternmen</h1>
  </main>
</body>
</html>
```